The maple crew

I want it as prefession and attractive as possible we are a lawnmowing business

Phone number 605-318-2264
Name- Carlos Whitfield
Email- themaplecrewsd@fernpost.com

```html
<!DOCTYPE html>
<html lang="en">
<head>
<meta charset="utf-8">
<title>The Maple Crew — Business Card</title>
<link href="https://fonts.googleapis.com/css2?family=Bebas+Neue&family=Montserrat:wght@500&family=Roboto:wght@400&display=swap" rel="stylesheet">
<style>
  :root {
    --bg: #262626;
    --forest: #075434;
    --forest-deep: #064a2e;
    --leaf: #4bb041;
    --paper: #f3f3f2;
    --white: #ffffff;
    --emboss: #2e7d3f;
  }
  * { margin: 0; padding: 0; box-sizing: border-box; }
  html, body { width: 1200px; height: 576px; overflow: hidden; background: var(--bg); }
  .canvas { position: relative; width: 1200px; height: 576px; }

  .card {
    position: absolute;
    top: 138px;
    width: 484px;
    height: 293px;
    border-radius: 11px;
    overflow: hidden;
  }

  /* Back side */
  .card-back { left: 102px; background: var(--forest); }
  .card-back .decor {
    position: absolute; left: 0; top: 0; width: 100%; height: 100%;
    background: radial-gradient(ellipse at 30% 55%, rgba(75,176,65,0.14), rgba(75,176,65,0) 60%);
  }
  .card-back .brand {
    position: absolute; left: 0; right: 0; top: 120px;
    display: flex; justify-content: center; align-items: center; gap: 10px;
  }
  .card-back .brand-mark { width: 18px; height: 18px; background: var(--emboss); }
  .card-back .brand-name {
    font-family: "Bebas Neue", sans-serif; font-size: 50px; line-height: 1;
    color: var(--emboss); letter-spacing: 1px;
  }
  .card-back .website {
    position: absolute; left: 0; right: 0; bottom: 20px; text-align: center;
    font-family: "Montserrat", sans-serif; font-weight: 500; font-size: 13px;
    letter-spacing: 3px; color: #d9e8dd;
  }

  /* Front side */
  .card-front { left: 596px; background: var(--paper); }
  .card-front .wave { position: absolute; left: 0; top: 0; width: 100%; height: 100%; }
  .card-front .brand {
    position: absolute; left: 28px; top: 80px;
    display: flex; align-items: center; gap: 9px;
  }
  .card-front .brand-mark { width: 15px; height: 15px; background: var(--forest); }
  .card-front .brand-name {
    font-family: "Bebas Neue", sans-serif; font-size: 38px; line-height: 1;
    color: var(--forest); letter-spacing: 1px;
  }
  .card-front .person {
    position: absolute; right: 32px; top: 48px;
    font-family: "Bebas Neue", sans-serif; font-weight: 400; font-size: 23px;
    line-height: 1; letter-spacing: 0.5px; white-space: nowrap;
  }
  .person .first { color: var(--forest); }
  .person .last { color: var(--leaf); }
  .contact {
    position: absolute; right: 32px; top: 217px;
    list-style: none;
    font-family: "Roboto", sans-serif; font-size: 12.5px; color: var(--white);
  }
  .contact li { display: flex; justify-content: flex-end; align-items: center; gap: 10px; height: 18px; }
  .contact svg { width: 12px; height: 12px; fill: var(--leaf); }
</style>
</head>
<body>
<main class="canvas">

  <section class="card card-back" aria-label="Card back">
    <div class="decor" role="img" aria-label="Faint illustration of a worker pushing a lawn mower"></div>
    <div class="brand">
      <span class="brand-mark"></span>
      <span class="brand-name">The Maple Crew</span>
    </div>
    <p class="website">www.maplecrewlawn.com</p>
  </section>

  <section class="card card-front" aria-label="Card front">
    <svg class="wave" viewBox="0 0 484 293" preserveAspectRatio="none" aria-hidden="true">
      <path d="M40 236 C 140 260, 220 250, 300 205 C 370 168, 420 135, 484 134 L484 146 C 420 148, 370 178, 305 214 C 220 262, 130 262, 40 236 Z" fill="var(--leaf)"/>
      <path d="M0 228 C 60 252, 150 268, 230 250 C 300 232, 360 178, 484 155 L484 293 L0 293 Z" fill="var(--forest)"/>
      <path d="M40 240 C 120 258, 200 252, 260 228 C 200 262, 110 264, 40 240 Z" fill="var(--leaf)"/>
    </svg>
    <div class="brand">
      <span class="brand-mark"></span>
      <span class="brand-name">The Maple Crew</span>
    </div>
    <h1 class="person"><span class="first">Carlos</span> <span class="last">Whitfield</span></h1>
    <ul class="contact">
      <li>605-318-2264
        <svg viewBox="0 0 24 24" aria-hidden="true"><path d="M6.6 10.8a15.1 15.1 0 0 0 6.6 6.6l2.2-2.2a1 1 0 0 1 1-.25 11.4 11.4 0 0 0 3.6.57 1 1 0 0 1 1 1V20a1 1 0 0 1-1 1A17 17 0 0 1 3 4a1 1 0 0 1 1-1h3.5a1 1 0 0 1 1 1c0 1.25.2 2.45.57 3.57a1 1 0 0 1-.25 1z"/></svg>
      </li>
      <li>themaplecrewsd@fernpost.com
        <svg viewBox="0 0 24 24" aria-hidden="true"><path d="M2 5h20v14H2z M3.5 6.5 12 13l8.5-6.5z" fill-rule="evenodd"/></svg>
      </li>
    </ul>
  </section>

</main>
</body>
</html>
```